Velvet Crumb by Marisol

Attached see my logo, i need to create a FB logo and banner to mirror my logo. My company does handcrafted and homemade gourmet pieces of heaven! Feel free to call me at 3127750146 or email me at marisol@velvetcrumb.com. Thank you. Marisol

```html
<!DOCTYPE html>
<html lang="en">
<head>
<meta charset="utf-8">
<title>Velvet Crumb by Marisol – Facebook Cover</title>
<link rel="stylesheet" href="https://fonts.googleapis.com/css2?family=Comfortaa:wght@300&family=Oswald:wght@500&display=swap">
<style>
  :root {
    --pink: #f29ac0;
    --mint: #d3ece8;
    --placeholder: #efe6ef;
    --placeholder-faint: rgba(220, 226, 228, 0.35);
    --purple: #9b6aa8;
    --frame-blue: #3b5998;
    --frame-grey: #cfd1d3;
    --white: #ffffff;
  }
  * { box-sizing: border-box; margin: 0; padding: 0; }
  html, body {
    width: 1200px; height: 492px; overflow: hidden; background: var(--white);
  }
  .cover {
    position: relative; width: 1200px; height: 492px; overflow: hidden; background: var(--white);
  }
  .cover__topline {
    position: absolute; left: 26px; top: 14px; width: 1152px; height: 3px;
    background: var(--frame-blue);
  }
  .cover__edge {
    position: absolute; left: 26px; top: 14px; width: 8px; height: 440px;
    background: #eef0f2;
  }
  .awning {
    position: absolute; left: 34px; width: 1146px;
    background: repeating-linear-gradient(90deg,
      var(--mint) 0 42px, var(--pink) 42px 90px, var(--mint) 90px 96px);
  }
  .awning--top { top: 18px; height: 84px; }
  .awning--bottom { top: 410px; height: 30px; }
  .stage {
    position: absolute; left: 34px; top: 102px; width: 1146px; height: 308px;
    background: linear-gradient(180deg, #ffffff 0%, #ffffff 8%, #f1f1f2 16%, #fbfbfb 55%, #f0f0f1 90%, #ffffff 100%);
  }
  .watermark {
    position: absolute; left: 330px; top: 170px;
    font-family: "Comfortaa", sans-serif; font-weight: 300;
    font-size: 110px; line-height: 1; letter-spacing: 4px;
    color: rgba(242, 154, 192, 0.18); white-space: nowrap;
  }
  .watermark-art {
    position: absolute; left: 484px; top: 128px; width: 118px; height: 216px;
    background: var(--placeholder-faint);
  }
  .brand {
    position: absolute; left: 600px; top: 50px; width: 560px; height: 260px;
  }
  .brand__art {
    position: absolute; left: 80px; top: 0; width: 140px; height: 140px;
    background: var(--placeholder);
  }
  .brand__name {
    position: absolute; left: 0; top: 150px;
    font-family: "Comfortaa", sans-serif; font-weight: 300;
    font-size: 80px; line-height: 1; color: var(--pink); white-space: nowrap;
  }
  .actions {
    position: absolute; left: 790px; top: 314px; display: flex; gap: 8px;
  }
  .action {
    position: relative; width: 96px; height: 54px;
    border: 3px solid var(--pink); border-radius: 6px;
    background: linear-gradient(180deg, #ffffff 0%, #e9e9ea 55%, #d6d6d8 100%);
    font-family: "Oswald", sans-serif; font-weight: 500; font-size: 20px;
    color: var(--purple); display: flex; align-items: center; justify-content: center;
  }
  .action::after {
    content: ""; position: absolute; bottom: -11px; left: 26px;
    border-left: 6px solid transparent; border-right: 6px solid transparent;
    border-top: 9px solid var(--pink);
  }
  .action--follow::after { left: 42px; }
  .action--message::after { left: 68px; }
  .profile {
    position: absolute; left: 54px; top: 254px; width: 228px; height: 206px;
    border: 6px solid var(--frame-grey); background: var(--white); overflow: hidden;
  }
  .profile__stripes {
    position: absolute; left: 0; bottom: 0; width: 100%; height: 44px;
    background: repeating-linear-gradient(90deg,
      var(--pink) 0 48px, var(--mint) 48px 96px);
  }
  .profile__ring { position: absolute; left: 0; top: 0; }
  .profile__art {
    position: absolute; left: 64px; top: 38px; width: 92px; height: 116px;
    background: var(--placeholder);
  }
</style>
</head>
<body>
<main class="cover">
  <div class="cover__topline"></div>
  <div class="cover__edge"></div>
  <div class="awning awning--top"></div>
  <div class="stage"></div>
  <div class="awning awning--bottom"></div>

  <div class="watermark" aria-hidden="true">Velvet Crumb</div>
  <div class="watermark-art" role="img" aria-label="Faint cupcake illustration in the background"></div>

  <div class="brand">
    <div class="brand__art" role="img" aria-label="Cupcake illustration"></div>
    <div class="brand__name">Velvet Crumb</div>
  </div>

  <nav class="actions">
    <div class="action action--like">LIKE</div>
    <div class="action action--follow">FOLLOW</div>
    <div class="action action--message">MESSAGE</div>
  </nav>

  <div class="profile">
    <div class="profile__stripes"></div>
    <svg class="profile__ring" width="216" height="194" viewBox="0 0 216 194" aria-hidden="true">
      <circle cx="108" cy="100" r="86" fill="rgba(255,255,255,0.55)" stroke="#f29ac0" stroke-width="2" stroke-dasharray="10 6"/>
    </svg>
    <div class="profile__art" role="img" aria-label="Cupcake illustration"></div>
  </div>
</main>
</body>
</html>
```